Kestrel Roofing & Restoration Business Card Design

Lookiing for a double sided business card design that will have rounded corners, will look good with Spot UV, Soft Laminate, or Gloss
Front of card should have Logo, Name and Contact Info, License numbers
Back of card should have Logo, maybe other small details

```html
<!DOCTYPE html>
<html lang="en">
<head>
<meta charset="utf-8">
<title>Kestrel Roofing &amp; Restoration – Business Cards</title>
<link rel="stylesheet" href="https://fonts.googleapis.com/css2?family=Poppins:wght@400;600&display=swap">
<style>
  :root {
    --card-black: #000000;
    --brand-blue: #19abe2;
    --ink-white: #ffffff;
    --backdrop: #d6d6d6;
  }
  * { margin: 0; padding: 0; box-sizing: border-box; }
  html, body {
    width: 1199px;
    height: 1200px;
    overflow: hidden;
    background: var(--backdrop);
    font-family: "Poppins", sans-serif;
  }
  .card {
    position: absolute;
    left: 176px;
    width: 848px;
    height: 496px;
    background: var(--card-black);
    overflow: hidden;
  }
  .card--front { top: 74px; }
  .card--back { top: 632px; }

  /* Front */
  .front__top-band {
    position: absolute;
    left: 425px; top: 0;
    width: 423px; height: 45px;
    background: var(--brand-blue);
  }
  .brand {
    position: absolute;
    display: flex;
    align-items: center;
    color: var(--ink-white);
    font-weight: 600;
    text-transform: uppercase;
    line-height: 1.12;
    white-space: nowrap;
  }
  .brand__square {
    flex: none;
    background: var(--brand-blue);
  }
  .card--front .brand { left: 86px; top: 103px; font-size: 34px; gap: 20px; }
  .card--front .brand__square { width: 60px; height: 60px; }

  .front__info-panel {
    position: absolute;
    left: 0; top: 254px;
    width: 672px; height: 242px;
    background: var(--brand-blue);
    color: var(--ink-white);
    padding: 22px 0 0 80px;
  }
  .person-name {
    font-weight: 600;
    font-size: 34px;
    line-height: 1.2;
    margin-bottom: 22px;
  }
  .contact-list { list-style: none; font-size: 21px; font-weight: 400; }
  .contact-list li { display: flex; height: 36px; align-items: center; white-space: nowrap; }
  .contact-list .label { width: 34px; }
  .contact-list .value::before { content: ": "; }

  /* Back */
  .back__side-block {
    position: absolute;
    left: 0; top: 0;
    width: 151px; height: 496px;
    background: var(--brand-blue);
  }
  .back__side-notch {
    position: absolute;
    left: 94px; top: 99px;
    width: 57px; height: 297px;
    background: var(--card-black);
  }
  .card--back .brand { left: 232px; top: 196px; font-size: 43px; gap: 24px; }
  .card--back .brand__square { width: 74px; height: 74px; }
</style>
</head>
<body>
  <section class="card card--front" aria-label="Front of business card">
    <div class="front__top-band"></div>
    <div class="brand">
      <span class="brand__square"></span>
      <span class="brand__name">Kestrel Roofing<br>&amp; Restoration</span>
    </div>
    <div class="front__info-panel">
      <p class="person-name">YOUR NAME</p>
      <ul class="contact-list">
        <li><span class="label">M</span><span class="value">555 014 2290</span></li>
        <li><span class="label">W</span><span class="value">www.kestrelroofingco.com</span></li>
        <li><span class="label">A</span><span class="value">418 Cedar Hollow Lane, Marlow Springs, OK 73154</span></li>
      </ul>
    </div>
  </section>

  <section class="card card--back" aria-label="Back of business card">
    <div class="back__side-block"></div>
    <div class="back__side-notch"></div>
    <div class="brand">
      <span class="brand__square"></span>
      <span class="brand__name">Kestrel Roofing<br>&amp; Restoration</span>
    </div>
  </section>
</body>
</html>
```